Structural Engineering Company needs ad for magazine

We are an engineering office for structural engineering in the entertainment industry. Our focus are concert stages, festival structures, grand stands and exhibition booths. Our customers are mainly from Europe, we realize the projects worldwide. Typical customers are designer, architects, stage builders, exhibition builder and technical service provider. We are creating structural analyses, technical consulting, technical drawings and risk assessment. We are working on mid size and major events.
Some technical notes:
- CMYK profile needed, minimum 300 dpi for raster graphic
- Our primary color is Petrol. Favourite is petrol, coral and grey (black). Please use palette shown below.
- Our font in documents is Myriad. Regular at 10 pt for text and Light at 16-24pt for titles.
- The format for the ad is 61 x 127 mm (portrait) or 185 x 46 mm (landscape). Which one is up to you.
To the content:
- For contact details we just want to provide our web address "belsokar.de" and/or our e-mail "info@belsokar.de"
- Attached are some Logo files and photos.
- The ad do not advertise a specific product. It is more a general advertisement for the company.
- The language for the ad should be German. Below are keywords in English and corresponding German translation. You do not need to place all Keywords, it is just a brainstorming list to help you. You are also welcome to use other text. We will help with translation, if necessary.
- we like discussing ideas to get better results, so also if you have questions, please ask.
- If you need information that we haven't thought of yet, please ask.
Our slogan (also in Germany): event meets engineering
Service Keywords EN / DE
- Structural Analysis / Statische Berechnungen
- Risk Assessment / Risikobewertungen
- Consulting & Design / Beratung & Konstruktion
Technical Keywords EN / DE
- Stage machinery / Bühnentechnik
- Scaffolding / Gerüstbau
- Exhibition Booths / Messebauten
- Tents / Zelte
- Temporary Structures / Fliegende Bauten
- Truss / Traversen
- Stages / Bühnen
- Grand Stands / Tribünen
- Leightweight Construction / Leichtbau
- Steel Construction / Stahlbau
- Amusement Rides / Fahrgeschäfte
Look and feel
Each slider illustrates characteristics of the customer's brand and the style your logo design should communicate.

```html
<!DOCTYPE html>
<html lang="de">
<head>
<meta charset="utf-8">
<title>Belsokar Engineering – Anzeige</title>
<link rel="stylesheet" href="https://fonts.googleapis.com/css2?family=PT+Sans:wght@700&family=Montserrat:wght@400;500&display=swap">
<style>
  :root {
    --ink: #111111;
    --teal: #5fe0d6;
    --paper: #ffffff;
    --photo-sky: #cfd6dc;
    --photo-blue: #4f6fc9;
    --photo-mint: #63d6c2;
    --photo-grey: #b9bfc4;
  }
  html, body { margin: 0; padding: 0; overflow: hidden; }
  .ad {
    position: relative;
    width: 1200px;
    height: 299px;
    background: var(--paper);
    overflow: hidden;
  }
  .ad__photo {
    position: absolute;
    left: 412px; top: 0; right: 0; bottom: 0;
    background:
      linear-gradient(90deg, var(--paper) 0%, rgba(255,255,255,0.6) 12%, rgba(255,255,255,0) 28%),
      linear-gradient(180deg, var(--photo-sky) 0%, var(--photo-blue) 35%, var(--photo-mint) 55%, var(--photo-blue) 68%, var(--photo-grey) 80%, #d9dcde 100%);
  }
  .services {
    position: absolute;
    left: 18px; top: 10px;
    margin: 0;
    font-family: "PT Sans", sans-serif;
    font-weight: 700;
    font-size: 25px;
    line-height: 26.5px;
    color: var(--ink);
  }
  .keywords {
    position: absolute;
    left: 18px; top: 108px;
    margin: 0; padding: 0;
    list-style: none;
    font-family: "Montserrat", sans-serif;
    font-weight: 500;
    font-size: 14.5px;
    line-height: 19px;
    color: var(--teal);
  }
  .contact {
    position: absolute;
    left: 164px; top: 257px;
    font-family: "Montserrat", sans-serif;
    font-weight: 400;
    font-size: 21px;
    color: var(--ink);
  }
  .brand {
    position: absolute;
    left: 1050px; top: 18px;
    width: 140px; height: 140px;
    border-radius: 50%;
    background: var(--paper);
    display: flex; align-items: center; justify-content: center;
    font-family: "Montserrat", sans-serif;
    font-weight: 500;
    font-size: 15px;
    letter-spacing: 2px;
    color: var(--ink);
  }
</style>
</head>
<body>
  <div class="ad">
    <div class="ad__photo" role="img" aria-label="Foto: Bühnenaufbau in einem Stadion mit Traversentürmen, gelbem Mobilkran und Gabelstapler vor blau-türkisen Tribünen"></div>

    <h1 class="services">Statische Berechnungen,<br>Risikobewertungen, Beratung<br>Konstruktion</h1>

    <ul class="keywords">
      <li>Stahlbau</li>
      <li>Leichtbau</li>
      <li>Bühnen</li>
      <li>Messebauten</li>
      <li>Zelte</li>
      <li>Gerüstbau</li>
      <li>Bühnentechnik</li>
      <li>Fliegende Bauten</li>
      <li>und aber viel...</li>
    </ul>

    <div class="contact">info@belsokar.de</div>

    <div class="brand">BELSOKAR</div>
  </div>
</body>
</html>
```